Digital One Pager for Consulting Practice

I would like the essence of the content in my ppt consolidated into a one-pager. The one-pager will mainly be sent via email as a pdf and intended to excite and invite new clients and establish the credibility of my boutique high-end consulting firm. Infographics and symbols would be a plus. The target client should view the firm as providing premeir service. The client is getting a thought partner.

Target Market(s)

Large Medical Device Manufacturer Executives, Early-Stage Medical Device Manufacturer Executives, Partners at VC Firms

Industry/Entity Type

Medical Equipment

Colors
0355a3
f37122

Requirements
Must have
• Please match the color scheme in ppt. Please use the existing logo. I am very open to better graphics on the process. My photo does not need to be on the digital flyer. Hyper link to the website and email is needed.
Nice to have
• Infographics

```html
<!DOCTYPE html>
<html lang="en">
<head>
<meta charset="utf-8">
<title>Kestrel Ventures – One Pager</title>
<link rel="stylesheet" href="https://fonts.googleapis.com/css2?family=Montserrat:wght@700&family=Roboto:wght@400;500&family=Roboto+Condensed:wght@700&family=Russo+One&family=Share+Tech+Mono&family=PT+Serif:wght@700&display=swap">
<style>
  :root{
    --navy:#1b2a44;
    --blue:#0355a3;
    --orange:#f37122;
    --white:#ffffff;
    --ink:#1f1f1f;
    --shadow:#b9bcc2;
  }
  html,body{margin:0;padding:0;overflow:hidden;background:var(--white);}
  .page{position:relative;width:927px;height:1200px;overflow:hidden;background:var(--white);font-family:"Roboto",Arial,sans-serif;}
  .artwork{position:absolute;left:0;top:0;width:927px;height:1200px;}
  .brand{position:absolute;left:60px;top:38px;display:flex;align-items:center;gap:16px;}
  .brand-dot{width:30px;height:30px;border-radius:50%;background:var(--orange);flex:none;}
  .brand-name{font-family:"Montserrat",Arial,sans-serif;font-weight:700;font-size:42px;letter-spacing:4px;color:var(--navy);line-height:46px;}
  .value{position:absolute;left:540px;top:303px;width:326px;color:var(--white);}
  .value-title{font-family:"Russo One",sans-serif;font-weight:400;font-size:21px;letter-spacing:0.5px;margin:0 0 10px;white-space:nowrap;}
  .value-list{list-style:none;margin:0;padding:0;text-align:right;font-family:"Share Tech Mono",monospace;font-size:20px;line-height:34px;letter-spacing:1px;}
  .column{position:absolute;top:556px;}
  .column h2{font-family:"Roboto",Arial,sans-serif;font-weight:500;font-size:33px;margin:0 0 6px;color:var(--ink);}
  .column p{margin:0;font-family:"Roboto Condensed",Arial,sans-serif;font-weight:700;font-size:16px;line-height:25.5px;color:var(--ink);}
  .column .sub{padding-left:52px;}
  .column--experience{right:491px;width:400px;text-align:right;}
  .column--offer{left:497px;width:400px;}
  .divider{position:absolute;left:465px;top:566px;width:4px;height:314px;background:var(--orange);}
  .footer{position:absolute;left:0;bottom:0;width:927px;height:52px;display:flex;align-items:center;justify-content:center;
    font-family:"Roboto",Arial,sans-serif;font-size:22px;color:var(--white);white-space:nowrap;}
  .footer a{color:var(--white);text-decoration:none;}
  .footer .sep{margin:0 8px;}
</style>
</head>
<body>
<div class="page">
  <svg class="artwork" viewBox="0 0 612 792" xmlns="http://www.w3.org/2000/svg">
    <!-- top right panel -->
    <polygon points="268,182 612,298 612,362" fill="var(--orange)"/>
    <polygon points="398,0 612,0 612,332 340,292" fill="var(--navy)"/>

    <!-- leverage hexagons -->
    <g class="leverage">
      <polygon points="463,55 480,26 514,26 531,55 514,84 480,84" fill="var(--orange)"/>
      <polygon points="423,122 440,93 474,93 491,122 474,151 440,151" fill="var(--orange)"/>
      <polygon points="503,122 520,93 554,93 571,122 554,151 520,151" fill="var(--orange)"/>
      <circle cx="497" cy="102" r="34" fill="var(--white)" stroke="var(--navy)" stroke-width="3"/>
      <text x="497" y="106" text-anchor="middle" font-family="PT Serif,serif" font-weight="700" font-size="11" fill="var(--navy)">LEVERAGE</text>
      <text x="497" y="47" text-anchor="middle" font-family="Roboto,Arial,sans-serif" font-size="9.5" fill="var(--white)">Process</text>
      <text transform="translate(444,126) rotate(62)" text-anchor="middle" font-family="Roboto,Arial,sans-serif" font-size="9.5" fill="var(--white)">Experience</text>
      <text transform="translate(550,126) rotate(-62)" text-anchor="middle" font-family="Roboto,Arial,sans-serif" font-size="9.5" fill="var(--white)">Network</text>
    </g>

    <!-- services infographic -->
    <g class="services" font-family="PT Serif,serif">
      <path d="M100,195 L222,150 M95,318 L215,290 M100,195 L215,290 M222,150 L95,318" stroke="var(--orange)" stroke-width="14"/>
      <path d="M100,195 L222,150 M95,318 L215,290 M100,195 L215,290 M222,150 L95,318" stroke="var(--blue)" stroke-width="6"/>
      <circle cx="100" cy="195" r="52" fill="var(--blue)" stroke="var(--orange)" stroke-width="4"/>
      <circle cx="222" cy="150" r="52" fill="var(--blue)" stroke="var(--orange)" stroke-width="4"/>
      <circle cx="95" cy="320" r="52" fill="var(--blue)" stroke="var(--orange)" stroke-width="4"/>
      <circle cx="215" cy="290" r="52" fill="var(--blue)" stroke="var(--orange)" stroke-width="4"/>

      <text x="100" y="182" text-anchor="middle" font-weight="700" font-size="9.5" fill="var(--white)">Regulatory Strategy</text>
      <text x="100" y="199" text-anchor="middle" font-family="Roboto,Arial,sans-serif" font-size="6.5" fill="var(--orange)">* RAQA Organizational</text>
      <text x="100" y="211" text-anchor="middle" font-family="Roboto,Arial,sans-serif" font-size="6.5" fill="var(--orange)">Structure</text>
      <text x="100" y="223" text-anchor="middle" font-family="Roboto,Arial,sans-serif" font-size="6.5" fill="var(--orange)">* Regulatory Pathway</text>

      <text x="222" y="146" text-anchor="middle" font-weight="700" font-size="9.5" fill="var(--white)">FDA Communication</text>
      <text x="222" y="165" text-anchor="middle" font-family="Roboto,Arial,sans-serif" font-size="6.5" fill="var(--orange)">* Deficiency Responce</text>
      <text x="222" y="177" text-anchor="middle" font-family="Roboto,Arial,sans-serif" font-size="6.5" fill="var(--orange)">* Aplication Review</text>

      <text x="95" y="305" text-anchor="middle" font-weight="700" font-size="9.5" fill="var(--white)">Interim Executive</text>
      <text x="95" y="317" text-anchor="middle" font-weight="700" font-size="9.5" fill="var(--white)">Leadership</text>
      <text x="95" y="335" text-anchor="middle" font-family="Roboto,Arial,sans-serif" font-size="6.5" fill="var(--orange)">* Compliance Remedition</text>
      <text x="95" y="347" text-anchor="middle" font-family="Roboto,Arial,sans-serif" font-size="6.5" fill="var(--orange)">* Accelerated Product</text>
      <text x="95" y="359" text-anchor="middle" font-family="Roboto,Arial,sans-serif" font-size="6.5" fill="var(--orange)">Registration</text>

      <text x="215" y="278" text-anchor="middle" font-weight="700" font-size="9.5" fill="var(--white)">Training</text>
      <text x="215" y="296" text-anchor="middle" font-family="Roboto,Arial,sans-serif" font-size="6.5" fill="var(--orange)">* FDA Communication</text>
      <text x="215" y="308" text-anchor="middle" font-family="Roboto,Arial,sans-serif" font-size="6.5" fill="var(--orange)">* MDR Reporting</text>

      <g transform="translate(158,240) rotate(-20)">
        <rect x="-34" y="-10" width="68" height="20" fill="var(--white)" stroke="var(--orange)" stroke-width="3"/>
        <text x="0" y="4.5" text-anchor="middle" font-family="Roboto,Arial,sans-serif" font-size="12" fill="var(--blue)">SERVICES</text>
      </g>
    </g>

    <!-- efficiency band -->
    <polygon points="115,616 150,572 612,600 612,616" fill="var(--orange)"/>
    <text x="145" y="604" font-family="Roboto,Arial,sans-serif" font-weight="500" font-size="12.5" fill="var(--white)">Effecience Process</text>
    <polygon points="45,618 612,618 612,758 0,758 0,656" fill="var(--navy)"/>

    <!-- process steps -->
    <g class="process" font-family="Roboto,Arial,sans-serif" font-size="10" text-anchor="middle" fill="var(--white)">
      <circle cx="196" cy="690" r="45" fill="var(--shadow)"/>
      <circle cx="290" cy="690" r="45" fill="var(--shadow)"/>
      <circle cx="384" cy="690" r="45" fill="var(--shadow)"/>
      <circle cx="478" cy="690" r="45" fill="var(--shadow)"/>
      <circle cx="187" cy="688" r="44" fill="var(--blue)" stroke="var(--white)" stroke-width="1.5"/>
      <circle cx="281" cy="688" r="44" fill="var(--orange)" stroke="var(--white)" stroke-width="1.5"/>
      <circle cx="375" cy="688" r="44" fill="var(--blue)" stroke="var(--white)" stroke-width="1.5"/>
      <circle cx="469" cy="688" r="44" fill="var(--orange)" stroke="var(--white)" stroke-width="1.5"/>
      <polygon points="230,680 240,680 248,688 240,696 230,696" fill="var(--blue)"/>
      <polygon points="324,680 334,680 342,688 334,696 324,696" fill="var(--orange)"/>
      <polygon points="418,680 428,680 436,688 428,696 418,696" fill="var(--blue)"/>
      <text x="187" y="686">Exploratory</text><text x="187" y="699">Call</text>
      <text x="281" y="686">Regulatory</text><text x="281" y="699">Landscape</text>
      <text x="375" y="686">Problem</text><text x="375" y="699">Statement</text>
      <text x="469" y="680">Review &amp; Align</text><text x="469" y="693">on</text><text x="469" y="706">Deliverables</text>
    </g>

    <!-- footer band -->
    <rect x="0" y="758" width="612" height="34" fill="var(--orange)"/>
  </svg>

  <div class="brand"><span class="brand-dot"></span><div class="brand-name">KESTREL<br>VENTURES</div></div>

  <div class="value">
    <h1 class="value-title">KESTREL VENTURES VALUE</h1>
    <ul class="value-list">
      <li>Extensive Experience</li>
      <li>Efficient Process</li>
      <li>Valued Network</li>
    </ul>
  </div>

  <section class="column column--experience">
    <h2>Experince</h2>
    <p>&gt; Over decade @FDA (Former Deputy</p>
    <p>Devision Director)</p>
    <p>&gt; Expertise Cardiovascular, Ophthalmology,</p>
    <p>General Hospital, Infection Control,</p>
    <p>Dental, Anesthesia, Respiratory</p>
    <p>&gt; Vice President Regulatory Affairs/</p>
    <p>Quality Assurance @Corvane (Fortune</p>
    <p>150 Company)</p>
  </section>

  <div class="divider"></div>

  <section class="column column--offer">
    <h2>Experince to Provide</h2>
    <p>&gt; Executive Application Review</p>
    <p class="sub">* Examples Includes : Presubmission,</p>
    <p class="sub">IDE, 510(k), 513(g), PMA, Refuse to</p>
    <p class="sub">Accept, Hold Letter</p>
    <p class="sub">* Troubleshooting</p>
    <p>&gt; Strategic Advice &amp; Diligence to Investors</p>
    <p class="sub">* Validate &amp; Verify Founder Milestones</p>
    <p class="sub">* Diligence Portfolio Company</p>
    <p class="sub">Regulatory and Quality System</p>
  </section>

  <footer class="footer">
    <a href="https://www.kestrelventures-advisory.com">www.kestrelventures-advisory.com</a>
    <span class="sep">|</span><span>202.555.0147</span><span class="sep">|</span>
    <a href="mailto:hello@kestrelventures-advisory.com">hello@kestrelventures-advisory.com</a>
  </footer>
</div>
</body>
</html>
```